Advanced Therapeutic Massage Therapist

I need a business card advertising my massage services as an advanced therapeutic massage therapist. I offer advanced therapeutic massage, swedish and deep tissue. I want to create a simple, professional and feminine card. I like bright colours and creativity.

I prefer a bold and experimental approach rather than something status-quo. A card to suggest therapeutic healing through dynamic massage. Motifs, shapes or layout which suggest movement and flow.
Updates

Target Market(s)

Everybody!

Industry/Entity Type

Health And Wellness

Contact Information for Business Card

The card should include:
My name, logo, services offered and my contact details.

Aoibhín Delaney
Massage Therapist

- Swedish - Deep Tissue - Advanced Therapeutic

Phone: (+353) 87 261 9043
Email: regenerate@aoibhindelaney-example.com
Website: www.aoibhindelany-example.com

Font styles to use
Serif
Sans Serif
Decorative
Script

Colors

Designer to choose colors to be used in the design.

Requirements
Must have
• An example may contain something like this, yet concise:
• "Aoibhín Delaney
• Massage Therapist
• - Swedish - Deep Tissue - Advanced Therapeutic"
Nice to have
• This sentence is optional:
• Imagery such as a logo or symbol. I have attached a file containing a logo I had produced however the name is incorrect now as it is "Aoibhín" not "Evie". It could be edited to change it to Aoibhín.
• I have sent the file as .psd .jpg. .pdf and .png
• I like when the card conveys energy, movement, pressure points, flow etc.
• I just like the designer to follow their own style and ideas. I like bright colours but must have a lot of a base colour to offset it. I really prefer them to follow their own inspiration. That is my preference.
Should not have
• Pine trees, non-native trees to Britain and Ireland, exotic flowers or animals that are not native to Britain and Ireland.
• I don't like brown as the background colour of the card.
• The cars shouldn't look like a wedding invitation i.e too many floral type designs.

```html
<!DOCTYPE html>
<html lang="en">
<head>
<meta charset="utf-8">
<title>Aoibhín Delaney – Massage Therapist Business Card</title>
<link href="https://fonts.googleapis.com/css2?family=Source+Sans+3:wght@400;500&display=swap" rel="stylesheet">
<style>
  :root {
    --page-bg: #ffffff;
    --card-bg: #ffffff;
    --ink: #2a2a2a;
    --ink-soft: #3c3c3c;
    --shadow: rgba(0, 0, 0, 0.14);
    --orange: #f58a12;
    --amber: #f7a20f;
    --red: #e8352a;
    --magenta: #b0198a;
    --purple: #8a1f9a;
    --indigo: #33309a;
    --mark: #9fc9bf;
  }
  * { margin: 0; padding: 0; box-sizing: border-box; }
  html, body {
    width: 1200px;
    height: 740px;
    overflow: hidden;
    background: var(--page-bg);
  }
  .canvas {
    position: relative;
    width: 1200px;
    height: 740px;
    font-family: "Source Sans 3", "Helvetica Neue", Arial, sans-serif;
    color: var(--ink);
  }
  .card {
    position: absolute;
    top: 114px;
    width: 306px;
    height: 506px;
    box-shadow: 0 1px 6px var(--shadow);
  }
  .card--front {
    left: 256px;
    background:
      radial-gradient(ellipse 45% 28% at 78% 30%, var(--amber) 0%, rgba(247,162,15,0) 100%),
      radial-gradient(ellipse 40% 22% at 25% 5%, #d8251f 0%, rgba(216,37,31,0) 100%),
      radial-gradient(ellipse 55% 30% at 20% 78%, var(--indigo) 0%, rgba(51,48,154,0) 100%),
      radial-gradient(ellipse 60% 25% at 15% 100%, #28309a 0%, rgba(40,48,154,0) 100%),
      radial-gradient(ellipse 45% 20% at 75% 80%, #7a1f9e 0%, rgba(122,31,158,0) 100%),
      linear-gradient(180deg, var(--orange) 0%, #f06a1a 22%, var(--red) 38%, var(--magenta) 55%, var(--purple) 75%, #6a2598 100%);
  }
  .card--back {
    left: 632px;
    background: var(--card-bg);
  }
  .back__name {
    position: absolute;
    left: 34px;
    top: 30px;
    font-size: 16px;
    font-weight: 400;
  }
  .back__role {
    position: absolute;
    left: 34px;
    top: 66px;
    font-size: 16px;
  }
  .back__services {
    position: absolute;
    left: 34px;
    top: 115px;
    font-size: 14px;
    line-height: 22px;
    list-style: none;
    color: var(--ink-soft);
  }
  .back__contact {
    position: absolute;
    left: 34px;
    top: 206px;
    font-size: 14px;
    line-height: 21px;
    font-style: normal;
    color: var(--ink-soft);
  }
  .back__mark {
    position: absolute;
    left: 0;
    width: 100%;
    top: 312px;
    display: flex;
    flex-direction: column;
    align-items: center;
    gap: 8px;
  }
  .mark__dot {
    width: 84px;
    height: 84px;
    border-radius: 50%;
    background: var(--mark);
  }
  .mark__name {
    font-size: 13px;
    color: var(--ink-soft);
  }
  .back__qualification {
    position: absolute;
    left: 0;
    width: 100%;
    top: 456px;
    text-align: center;
    font-size: 18px;
    font-weight: 400;
  }
</style>
</head>
<body>
<main class="canvas">
  <section class="card card--front" role="img" aria-label="Soft flowing gradient of orange, red, magenta, purple and deep blue"></section>

  <section class="card card--back">
    <h1 class="back__name">Aoibhín Delaney</h1>
    <p class="back__role">Massage Therapist</p>
    <ul class="back__services">
      <li>Swedish -</li>
      <li>Deep Tissue -</li>
      <li>Advanced Therapeutic</li>
    </ul>
    <address class="back__contact">
      (+353) 87 261 9043<br>
      aoibhin@aoibhindelaney-example.com<br>
      www.aoibhindelany-example.com
    </address>
    <div class="back__mark">
      <span class="mark__dot" aria-hidden="true"></span>
      <span class="mark__name">Aoibhín Delaney</span>
    </div>
    <p class="back__qualification">CTMA qualified</p>
  </section>
</main>
</body>
</html>
```